Lumo4Kart - a fintech company - business card

We need a business card design for our Payments Technology company in Sydney, Australia. We provide business with payment solutions expanding across IN-STORE machines, online payment gateways and mobile payment solutions. We would like to see designs that are clean, classy and professional.
Target Market(s)
Business professionals, executives, c-suite
Industry/Entity Type
Fintech
Contact Information for Business Card
Will be on 400gsm. Logo will most likely be spot gloss unless designer recommends otherwise.
Font styles to use
Sans Serif
Requirements
Must have
- We need our website (lumo4kart.com.au), email (contact@lumo4kart.com.au), mobile (0432 587 904) and direct phone number (02 6815 3927) to feature on the card along with our logo (attached) and the words "IN-STORE | ONLINE | MOBILE"
- Font = Roboto

```html
<!DOCTYPE html>
<html lang="en">
<head>
<meta charset="utf-8">
<title>Lumo4Kart – Business Card</title>
<link href="https://fonts.googleapis.com/css2?family=Roboto:wght@400;500;700&display=swap" rel="stylesheet">
<style>
  :root {
    --brand-blue: #155f91;
    --text-grey: #6d6e71;
    --divider-grey: #6d6e71;
    --base-grey: #6b6c70;
    --paper: #ffffff;
  }
  * { margin: 0; padding: 0; box-sizing: border-box; }
  html, body {
    width: 1200px;
    height: 686px;
    overflow: hidden;
    background: var(--paper);
  }
  .card {
    position: relative;
    width: 1200px;
    height: 686px;
    background: var(--paper);
    font-family: "Roboto", Arial, sans-serif;
    color: var(--text-grey);
  }
  .brand-mark {
    position: absolute;
    left: 146px;
    top: 179px;
    width: 288px;
    height: 210px;
    border-radius: 50%;
    background: var(--brand-blue);
  }
  .brand-name {
    position: absolute;
    left: 48px;
    top: 430px;
    width: 480px;
    text-align: center;
    font-size: 84px;
    font-weight: 700;
    line-height: 1;
    letter-spacing: -1px;
    color: var(--base-grey);
  }
  .divider {
    position: absolute;
    left: 597px;
    top: 189px;
    width: 2px;
    height: 333px;
    background: var(--divider-grey);
  }
  .person {
    position: absolute;
    left: 659px;
    top: 183px;
  }
  .person-name {
    font-size: 38px;
    font-weight: 700;
    color: var(--brand-blue);
    line-height: 46px;
  }
  .person-role {
    font-size: 32px;
    font-weight: 400;
    color: var(--text-grey);
    line-height: 40px;
  }
  .contact-list {
    position: absolute;
    left: 659px;
    top: 294px;
    list-style: none;
  }
  .contact-item {
    display: flex;
    align-items: center;
    height: 55px;
    font-size: 33px;
    color: var(--text-grey);
  }
  .contact-icon {
    width: 38px;
    height: 38px;
    margin-right: 25px;
    fill: var(--brand-blue);
    flex: none;
  }
  .service-band {
    position: absolute;
    left: 0;
    top: 613px;
    width: 1200px;
    height: 65px;
    background: var(--brand-blue);
    display: flex;
    align-items: center;
    justify-content: center;
    color: var(--paper);
    font-size: 33px;
    font-weight: 400;
    letter-spacing: 20px;
    padding-left: 20px;
    white-space: nowrap;
  }
  .base-strip {
    position: absolute;
    left: 0;
    top: 678px;
    width: 1200px;
    height: 8px;
    background: var(--base-grey);
  }
</style>
</head>
<body>
<div class="card">
  <div class="brand-mark" aria-hidden="true"></div>
  <div class="brand-name">LUMO4KART</div>

  <div class="divider"></div>

  <div class="person">
    <div class="person-name">John Doe</div>
    <div class="person-role">CEO</div>
  </div>

  <ul class="contact-list">
    <li class="contact-item">
      <svg class="contact-icon" viewBox="0 0 24 24" aria-hidden="true">
        <g fill="none" stroke="#155f91" stroke-width="1.6">
          <circle cx="12" cy="12" r="10"/>
          <ellipse cx="12" cy="12" rx="4.5" ry="10"/>
          <line x1="12" y1="2" x2="12" y2="22"/>
          <line x1="2" y1="12" x2="22" y2="12"/>
          <path d="M4 6.5h16M4 17.5h16"/>
        </g>
      </svg>
      <span>lumo4kart.com.au</span>
    </li>
    <li class="contact-item">
      <svg class="contact-icon" viewBox="0 0 24 24" aria-hidden="true">
        <path d="M2 5h20v2.2l-10 6.3L2 7.2z"/>
        <path d="M2 9.4l10 6.3 10-6.3V19H2z"/>
      </svg>
      <span>contact@lumo4kart.com.au</span>
    </li>
    <li class="contact-item">
      <svg class="contact-icon" viewBox="0 0 24 24" aria-hidden="true">
        <path d="M7.5 1h9A1.5 1.5 0 0 1 18 2.5v19a1.5 1.5 0 0 1-1.5 1.5h-9A1.5 1.5 0 0 1 6 21.5v-19A1.5 1.5 0 0 1 7.5 1zM7.6 4v14.5h8.8V4zM12 19.6a1.3 1.3 0 1 0 0 2.6 1.3 1.3 0 0 0 0-2.6z"/>
      </svg>
      <span>0432 587 904</span>
    </li>
    <li class="contact-item">
      <svg class="contact-icon" viewBox="0 0 24 24" aria-hidden="true">
        <path d="M6.6 2.2l3 3.6c.5.6.4 1.4-.1 1.9L7.8 9.3c1.3 2.8 4 5.5 6.9 6.9l1.6-1.7c.5-.5 1.3-.6 1.9-.1l3.6 3c.6.5.7 1.4.2 2l-1.7 2c-.6.7-1.6 1-2.5.7C10.5 20 4 13.5 1.9 6.2c-.3-.9 0-1.9.7-2.5l2-1.7c.6-.5 1.5-.4 2 .2z"/>
      </svg>
      <span>02 6815 3927</span>
    </li>
  </ul>

  <div class="service-band">IN-STORE | ONLINE | MOBILE</div>
  <div class="base-strip"></div>
</div>
</body>
</html>
```